Tariq Goldsmiths Stationary Contest

Pakistan’s largest Jewellery, Diamond and luxury watches store requires professional stationery. We have a long list of are trusted clients since 1959, our third generation has successfully maintained and sustained the legacy and excellence in the sector.

We require stationery template as part of this contest. The stationery can be double sided.

We prefer a design that makes use of some of the premium business stationery printing options, such as foil stamping, embossing/debossing, painted edges, spot UV etc (doesn't have to use all these options, only what you feel works, but we are looking for a design that stands out and is memorable and these nice touches have that effect.)

We want an eye catching, innovative, high end professional looking stationery for an out of box design that blends well with our new logo (attached). We want the design to be an out of box solution, you may use any element to compliment the logo. You may consider incorporating watermark etc, highlighting our products (Gold and Diamond Jewellery in addition to Luxury watches)

Company details are as follows;

Company name: Tariq Goldsmiths
Contact Person: Farhan Qureshi
Designation: Business Development Consultant
Mobile: +92 333 815 6042
Email: farhanqureshi@mailvale.com
Website: www.tariqgoldsmiths.com

Target Market(s)

Matrimonial, Elite & Businesses class, Upmarket

Font styles to use
Other font styles liked:
• Designers choice

Colors

Designer to choose colors to be used in the design.

Requirements
Must have
• Look and feel: Upmarket, innovative, Modern, Professional, graceful, Elegant, designer stuff.
Nice to have
• Unique design

```html
<!DOCTYPE html>
<html lang="en">
<head>
<meta charset="utf-8">
<title>Tariq Goldsmiths Stationery</title>
<link rel="stylesheet" href="https://fonts.googleapis.com/css2?family=Montserrat:wght@600;700&family=Questrial&family=Open+Sans:wght@400&display=swap">
<style>
  :root {
    --bg-centre: #f7e152;
    --bg-edge: #e6a318;
    --paper: #f5ebd6;
    --gold: #e3a10e;
    --gold-deep: #d28f06;
    --ink: #2b2b2b;
    --ink-soft: #555049;
    --flap: #111111;
    --watermark: rgba(214, 178, 110, 0.22);
  }
  * { margin: 0; padding: 0; box-sizing: border-box; }
  html, body { width: 1200px; height: 1200px; overflow: hidden; }
  body {
    position: relative;
    background: radial-gradient(circle at 50% 48%, var(--bg-centre) 0%, #f0c533 45%, var(--bg-edge) 100%);
    font-family: "Questrial", "Century Gothic", sans-serif;
    color: var(--ink);
  }
  .sheet {
    position: absolute;
    background: var(--paper);
    overflow: hidden;
    box-shadow: 0 6px 8px rgba(90, 55, 0, 0.45), 0 0 0 2px rgba(170, 120, 20, 0.35);
  }
  .wordmark {
    display: flex; align-items: center; justify-content: center; gap: 6px;
    font-family: "Montserrat", sans-serif; font-weight: 600;
    color: var(--gold); text-transform: uppercase; letter-spacing: 0.06em;
  }
  .wordmark .dot { border-radius: 50%; background: var(--gold); flex: none; }
  .watermark {
    position: absolute; border-radius: 50%;
    background: radial-gradient(circle, var(--watermark) 0%, rgba(214,178,110,0.12) 60%, transparent 72%);
  }

  /* Letterhead */
  .letterhead { left: 246px; top: 166px; width: 290px; height: 384px; }
  .letterhead .wordmark { margin-top: 22px; font-size: 11px; }
  .letterhead .wordmark .dot { width: 9px; height: 9px; }
  .letter-body {
    position: absolute; left: 17px; right: 20px; top: 112px;
    font-family: "Open Sans", sans-serif; font-size: 5.6px; line-height: 9px; color: var(--ink-soft);
  }
  .letter-body p { margin-bottom: 8px; }
  .letterhead .footer-band { position: absolute; left: 0; right: 0; bottom: 0; height: 20px; background: var(--gold); }

  /* Folder */
  .folder { left: 670px; top: 156px; width: 304px; height: 402px; }
  .folder svg.curves { position: absolute; inset: 0; }
  .folder .wordmark { position: absolute; left: 0; right: 0; top: 178px; font-size: 17px; }
  .folder .wordmark .dot { width: 14px; height: 14px; }
  .folder .web {
    position: absolute; left: 0; right: 0; bottom: 9px; text-align: center;
    font-family: "Open Sans", sans-serif; font-size: 6px; letter-spacing: 0.2em; color: var(--ink);
  }

  /* Business cards */
  .card { top: 619px; width: 271px; height: 162px; }
  .card-front { left: 311px; }
  .card-back { left: 614px; }
  .card .stripe { position: absolute; inset: 0; }
  .card-front .content { position: absolute; left: 0; right: 0; top: 34px; text-align: center; }
  .card-front .company { font-family: "Montserrat", sans-serif; font-weight: 700; font-size: 12px; color: var(--ink); }
  .card-front .person { margin-top: 10px; font-size: 12px; }
  .card-front .role { font-size: 4.6px; color: var(--ink-soft); }
  .card-front .contact { margin-top: 9px; font-size: 7.2px; line-height: 9.5px; }
  .card-back .wordmark { position: absolute; left: 0; right: 0; top: 68px; font-size: 12px; }
  .card-back .wordmark .dot { width: 10px; height: 10px; }
  .card-back .web {
    position: absolute; left: 16px; bottom: 4px; font-family: "Open Sans", sans-serif;
    font-size: 5px; letter-spacing: 0.14em; color: var(--paper);
  }

  /* Envelopes */
  .envelope { top: 854px; width: 338px; height: 168px; }
  .envelope-back { left: 228px; }
  .envelope-front { left: 632px; }
  .envelope-back .flap { position: absolute; inset: 0; }
  .envelope-back .flap-name {
    position: absolute; left: 0; right: 0; top: 7px; text-align: center;
    font-family: "Montserrat", sans-serif; font-weight: 600; font-size: 6px; color: var(--gold);
    letter-spacing: 0.08em; text-transform: uppercase;
  }
  .envelope-front .wordmark { position: absolute; left: 14px; top: 38px; font-size: 11px; justify-content: flex-start; }
  .envelope-front .wordmark .dot { width: 9px; height: 9px; }
  .envelope-front .address {
    position: absolute; left: 14px; top: 124px; font-size: 5px; line-height: 6.4px; color: var(--ink);
  }
  .envelope-front .footer-band { position: absolute; left: 0; right: 0; bottom: 0; height: 9px; background: var(--gold); }
</style>
</head>
<body>

  <section class="sheet letterhead" aria-label="Letterhead">
    <div class="wordmark"><span class="dot"></span>Tariq Goldsmiths</div>
    <div class="letter-body">
      <p>Dear [Recipient],</p>
      <p>Thank you for your continued trust in our house and our craft. We look forward to serving you again soon.</p>
      <p>Our new bridal range is now on display at the store. Each piece is finished by hand in gold and fine diamonds for your family.</p>
      <p>We have also set aside private viewing hours for our valued clients with a simple call.</p>
      <p>Please contact us at any time for a fitting. We will be glad to help.</p>
      <p>Warm regards,<br>Farhan</p>
    </div>
    <div class="footer-band"></div>
  </section>

  <section class="sheet folder" aria-label="Presentation folder">
    <svg class="curves" viewBox="0 0 304 402" preserveAspectRatio="none">
      <path d="M0 0 H304 V18 C220 6 90 10 0 38 Z" fill="var(--gold)"/>
      <path d="M0 44 C90 16 220 12 304 24" fill="none" stroke="var(--gold)" stroke-width="1.6"/>
      <path d="M0 384 C60 352 200 334 304 340 V402 H0 Z" fill="var(--gold)"/>
      <path d="M0 376 C70 344 200 326 304 332" fill="none" stroke="var(--gold)" stroke-width="1.4"/>
    </svg>
    <div class="wordmark"><span class="dot"></span>Tariq Goldsmiths</div>
    <div class="web">www.tariqgoldsmiths.com</div>
  </section>

  <section class="sheet card card-front" aria-label="Business card front">
    <div class="watermark" role="img" aria-label="Faint brand watermark" style="left:60px;top:14px;width:130px;height:130px;"></div>
    <svg class="stripe" viewBox="0 0 271 162" preserveAspectRatio="none">
      <path d="M0 150 H271 V162 H0 Z" fill="var(--gold)"/>
      <path d="M0 143 H125 L138 150" fill="none" stroke="var(--gold)" stroke-width="1.2"/>
      <path d="M132 143 H271" fill="none" stroke="var(--gold)" stroke-width="1.2"/>
    </svg>
    <div class="content">
      <div class="company">Tariq Goldsmiths</div>
      <div class="person">Farhan Qureshi</div>
      <div class="role">Business Development Consultant</div>
      <div class="contact">
        14 Mall Road Arcade, Gulberg, Lahore, Pakistan<br>
        042-35410287-89 &nbsp;|&nbsp; +92 333 815 6042<br>
        farhanqureshi@mailvale.com &nbsp;|&nbsp; www.tariqgoldsmiths.com
      </div>
    </div>
  </section>

  <section class="sheet card card-back" aria-label="Business card back">
    <svg class="stripe" viewBox="0 0 271 162" preserveAspectRatio="none">
      <path d="M0 146 H120 L130 152 H271 V162 H0 Z" fill="var(--gold)"/>
      <path d="M125 145 H271" fill="none" stroke="var(--gold)" stroke-width="1.2"/>
    </svg>
    <div class="wordmark"><span class="dot"></span>Tariq Goldsmiths</div>
    <div class="web">www.tariqgoldsmiths.com</div>
  </section>

  <section class="sheet envelope envelope-back" aria-label="Envelope back">
    <div class="watermark" role="img" aria-label="Faint brand watermark" style="left:190px;top:6px;width:170px;height:170px;"></div>
    <svg class="flap" viewBox="0 0 338 168" preserveAspectRatio="none">
      <path d="M0 0 H338 L312 28 H26 Z" fill="var(--flap)"/>
    </svg>
    <div class="flap-name">Tariq Goldsmiths</div>
  </section>

  <section class="sheet envelope envelope-front" aria-label="Envelope front">
    <div class="watermark" role="img" aria-label="Faint brand watermark" style="left:200px;top:-4px;width:170px;height:170px;"></div>
    <div class="wordmark"><span class="dot"></span>Tariq Goldsmiths</div>
    <div class="address">
      14 Mall Road Arcade, Gulberg, Lahore, Pakistan<br>
      042-35410287-89 &nbsp;|&nbsp; +92 333 815 6042<br>
      farhanqureshi@mailvale.com &nbsp;|&nbsp; www.tariqgoldsmiths.com
    </div>
    <div class="footer-band"></div>
  </section>

</body>
</html>
```